Website will be built in Dot Net Nuke v5 so fonts used need to be system fonts and design needs to be convertible to DNN skins/containers.
There is an existing website www.tallowwraps.com.au that we are redesigning with a more updated look based on the below but we are open to deviations or suggestions as to layout.
Site Map
o Home
o Health/Nutrition
o Store Locator
o Products
o Leasing
o Partners
o About Us
o Contact Us
Marlow Design Brief
Colours: Purple and Orange as per attached logo
The website will be purely targeted to the consumer but also allow for franchise enquiry and access for leasing agents. It also needs to portray corporate credibility.
Homepage and a content page will be mocked up with dummy content (have attached some images that can be used)
Design needs to be fresh and funky, young, vibrant with a cool flash section on the homepage
Homepage design requirements:
- Top Left Corner - Marlow Wraps logo
- Next to the logo – a banner with the words “It's how we roll"
- Left Pane (Narrow) – 2 call to action buttons – Franchise Enquiry and Store Locator
- Middle Content Pane – Funky flash area with rotating images that roll away like a kebab to reveal the next image.
- Below Middle Content Pane – Latest News on left and some content on the right
- Right Pane – Logos of clients vertically
Footer - Website Design by BRISK Digital and Privacy Statement, Terms of Use, Login etc that are standard with Dot Net Nuke

```html
<!DOCTYPE html>
<html lang="en">
<head>
<meta charset="utf-8">
<title>Marlow Wraps – It's how we roll</title>
<link href="https://fonts.googleapis.com/css2?family=Comfortaa:wght@400;700&family=Arimo:wght@400;700&family=Mountains+of+Christmas:wght@400;700&family=Kalam:wght@400;700&display=swap" rel="stylesheet">
<style>
:root{
  --purple:#4a1d45;
  --orange:#f0641e;
  --cream:#f0efe3;
  --olive:#a8a68f;
  --white:#ffffff;
  --grey:#9b9b8c;
  --text:#8a8a7c;
  --dark:#3b2b38;
}
*{box-sizing:border-box;margin:0;padding:0}
html,body{width:868px;height:1200px;overflow:hidden}
body{position:relative;background:linear-gradient(var(--cream) 0 217px,var(--olive) 217px);font-family:Arimo,Arial,sans-serif;color:var(--text)}
.abs{position:absolute}
.brand-mark{left:102px;top:14px;width:46px;height:46px;border-radius:50%;background:var(--orange)}
.brand-name{left:60px;top:64px;font:700 19px Comfortaa,sans-serif;color:var(--purple);white-space:nowrap}
.brand-tag{left:90px;top:110px;font:20px Kalam,cursive;color:var(--purple)}
.slogan{left:254px;top:60px;font:700 32px "Mountains of Christmas",Kalam,cursive;color:var(--purple);white-space:nowrap}
.toplinks{right:49px;top:24px;font-size:9.5px;color:var(--purple)}
.search{left:540px;top:63px;width:244px;height:38px;border-radius:19px;background:var(--white);border:1px solid #ddd;padding:12px 22px;font:12px Comfortaa,sans-serif;color:#aaa}
.go{left:787px;top:64px;width:36px;height:36px;border-radius:50%;background:var(--purple);border:2px solid var(--orange);color:var(--white);font:700 13px Arimo,sans-serif;text-align:center;line-height:32px}
.panel{left:27px;top:155px;width:810px;height:985px;background:var(--white);border-radius:14px 14px 0 0;box-shadow:0 0 3px rgba(0,0,0,.25)}
.nav-home{left:39px;top:171px;width:131px;height:44px;background:var(--purple);border-radius:12px 12px 0 0;color:var(--white);font:700 15px Comfortaa,sans-serif;text-align:center;line-height:44px}
.nav-item{top:186px;font:15px Comfortaa,sans-serif;color:var(--purple);white-space:nowrap}
.hero{left:39px;top:218px;width:786px;height:381px;background:linear-gradient(135deg,#5a2a6a 0%,#7a3a8a 45%,#c45a2a 75%,#3a3030 100%)}
.dot{top:531px;width:34px;height:34px;border-radius:50%;background:var(--purple);border:2px solid var(--white)}
.dot.on{background:var(--orange)}
.recipe-tab{left:624px;top:258px;width:149px;height:90px;background:var(--purple);border-radius:75px 75px 0 0;color:var(--white);font:19px Comfortaa,sans-serif;text-align:center;padding-top:20px;line-height:20px}
.recipe{left:593px;top:325px;width:212px;height:240px;background:rgba(255,255,255,.92);border-radius:12px;padding:18px 16px}
.recipe h2{font:400 26px Comfortaa,sans-serif;color:var(--orange);margin-bottom:12px;white-space:nowrap}
.recipe p{font:700 12.5px Comfortaa,sans-serif;color:var(--grey);text-align:justify;line-height:14px;margin-bottom:12px}
.recipe p.dark{color:var(--purple)}
.pill-grey{display:inline-block;background:var(--grey);color:var(--white);border-radius:14px;padding:6px 12px;font:700 13px Comfortaa,sans-serif}
.card{top:616px;width:257px;height:161px;border-radius:12px;overflow:hidden;padding:10px 13px;color:var(--white)}
.card h3{font:400 22px Comfortaa,sans-serif;margin-bottom:10px;white-space:nowrap}
.card p{font-size:10.5px;line-height:15px;width:170px}
.card .dish{position:absolute;right:-14px;bottom:-26px;width:120px;height:120px;border-radius:50%;border:3px solid var(--white)}
.card .btn{position:absolute;left:16px;bottom:18px;background:var(--white);border-radius:13px;padding:5px 11px;font:700 13px Comfortaa,sans-serif}
.card.purple{left:38px;background:var(--purple)}
.card.orange{left:301px;background:var(--orange)}
.card.purple .btn{color:var(--orange)}
.card.orange .btn{color:var(--purple)}
.side-h{font:400 22px Comfortaa,sans-serif;color:var(--purple);white-space:nowrap}
.news-title{left:592px;top:667px;font:700 10.5px Arimo,sans-serif;color:var(--orange)}
.news-date{left:592px;top:682px;font:700 9.5px Arimo,sans-serif;color:var(--dark)}
.news-body{left:592px;top:697px;width:205px;font-size:10px;line-height:15.5px;text-align:justify}
.more{left:735px;top:759px;font:700 9.5px Arimo,sans-serif;color:var(--purple)}
.rule{left:590px;width:219px;height:1px;background:var(--purple)}
.field{left:589px;width:208px;height:22px;border:1px solid #ccc;font-size:10px;color:var(--dark);padding:5px 7px}
.submit{left:590px;top:906px;width:84px;height:26px;border-radius:13px;background:var(--purple);color:var(--white);font:700 13px Arimo,sans-serif;text-align:center;line-height:26px;letter-spacing:.5px}
.clients{left:594px;top:1007px;width:218px;height:108px;border:3px solid var(--purple);border-radius:12px;display:flex;align-items:center;justify-content:space-around}
.client{font:700 14px Comfortaa,sans-serif;color:var(--purple);display:flex;align-items:center;gap:5px}
.client i{display:block;width:12px;height:12px;background:var(--orange)}
.welcome{left:52px;top:802px;font:700 24px "Mountains of Christmas",Kalam,cursive;color:var(--purple);white-space:nowrap}
.intro{left:52px;top:858px;width:497px;font-size:10.5px;line-height:12.5px}
.intro p{margin-bottom:12px}
.services-h{left:52px;top:972px;font:400 18px Comfortaa,sans-serif;color:var(--orange)}
.services{top:1010px;list-style:none;font-size:10.5px;color:var(--purple)}
.services li{height:20px;text-decoration:underline;position:relative;padding-left:18px}
.services svg{position:absolute;left:0;top:1px}
.footer{left:52px;top:1160px;font-size:9.5px;color:var(--white)}
.social{top:1157px;width:24px;height:24px;border-radius:4px}
</style>
</head>
<body>
<div class="abs brand-mark"></div>
<div class="abs brand-name">Marlow Wraps</div>
<div class="abs brand-tag">get it in ya!</div>
<div class="abs slogan">“ It's how we roll ”</div>
<div class="abs toplinks">Home | Conatct Us | Login</div>
<div class="abs search">Enter Search Kyeword</div>
<div class="abs go">go!</div>

<div class="abs panel"></div>
<div class="abs nav-home">Home</div>
<div class="abs nav-item" style="left:194px">Health/Nutrition</div>
<div class="abs nav-item" style="left:338px">Store Locator</div>
<div class="abs nav-item" style="left:465px">Products</div>
<div class="abs nav-item" style="left:557px">Leasing</div>
<div class="abs nav-item" style="left:640px">Partners</div>
<div class="abs nav-item" style="left:727px">About Us</div>

<div class="abs hero" role="img" aria-label="Photo of a Marlow Wraps shop counter with menu boards and rotisseries"></div>
<div class="abs dot on" style="left:64px"></div>
<div class="abs dot" style="left:108px"></div>
<div class="abs dot" style="left:148px"></div>
<div class="abs dot" style="left:192px"></div>
<div class="abs recipe-tab">View<br>Recipe</div>
<div class="abs recipe">
  <h2>Shish Kebab</h2>
  <p>In 1989, Mr Sami Doral first Marlow Wraps (MW) shop in Parkline Shopping Centre, Brookvale Queensland.</p>
  <p class="dark">Marlow Wraps, The Gold Coast and Brisbane.</p>
  <span class="pill-grey">› Read More</span>
</div>

<div class="abs card purple">
  <h3>Gril Cooking</h3>
  <p>Queenslanders had not yet seen nor heard of a kebab. After a fierce sampling exercise...</p>
  <div class="dish" role="img" aria-label="Photo of a grilled dish" style="background:radial-gradient(#e7d27a,#b8442e)"></div>
  <span class="btn">› Read More</span>
</div>
<div class="abs card orange">
  <h3>Today’s Special</h3>
  <p>Queenslanders had not yet seen nor heard of a kebab. After a fierce sampling exercise...</p>
  <div class="dish" role="img" aria-label="Photo of falafel pieces on a plate" style="background:radial-gradient(#f4f0e0,#c49a3a)"></div>
  <span class="btn">› Read More</span>
</div>

<div class="abs side-h" style="left:590px;top:624px">Latest News</div>
<div class="abs news-title">SHISH KEBAB FRANCHISE</div>
<div class="abs news-date">26 Jan 2011</div>
<div class="abs news-body">It was a roaring success. To this day Marlow at Parkline, is recognised as one of the most successful kebab retail shops in the country....</div>
<div class="abs more">› Read More</div>
<div class="abs rule" style="top:786px"></div>
<div class="abs side-h" style="left:590px;top:799px">Franchise Enquiry</div>
<div class="abs field" style="top:837px">Name:</div>
<div class="abs field" style="top:867px">E-mail:</div>
<div class="abs submit">SUBMIT</div>
<div class="abs rule" style="top:959px"></div>
<div class="abs side-h" style="left:590px;top:973px">Our Clients</div>
<div class="abs clients">
  <span class="client"><i></i>Hen House</span>
  <span class="client">Goldline</span>
</div>

<div class="abs welcome">Welcome to MARLOW WRAPS!</div>
<div class="abs intro">
  <p>In 1989, Mr Sami Doral launched the first Marlow Wraps (MW) shop in Parkline Shopping Centre, Brookvale Queensland.</p>
  <p>Queenslanders had not yet seen nor heard of a kebab. After a fierce sampling exercise, Queenslanders embraced Marlow Wraps. It was a roaring success. To this day Marlow at Parkline, is recognised as one of the most successful kebab retail shops in the country.</p>
  <p>Within 3 years Marlow Wraps was operating in 4 locations between the Gold Coast and Brisbane.</p>
</div>
<div class="abs services-h">Our Special Services</div>
<ul class="abs services" style="left:64px">
  <li><svg width="9" height="10"><path d="M1 1l6 4-6 4" fill="none" stroke="#f0641e" stroke-width="2.4"/></svg>Customers with value-added service</li>
  <li><svg width="9" height="10"><path d="M1 1l6 4-6 4" fill="none" stroke="#f0641e" stroke-width="2.4"/></svg>With Kebab products</li>
  <li><svg width="9" height="10"><path d="M1 1l6 4-6 4" fill="none" stroke="#f0641e" stroke-width="2.4"/></svg>Falafel options</li>
  <li><svg width="9" height="10"><path d="M1 1l6 4-6 4" fill="none" stroke="#f0641e" stroke-width="2.4"/></svg>Potato variations, sweets</li>
  <li><svg width="9" height="10"><path d="M1 1l6 4-6 4" fill="none" stroke="#f0641e" stroke-width="2.4"/></svg>Beverages</li>
</ul>
<ul class="abs services" style="left:324px">
  <li><svg width="9" height="10"><path d="M1 1l6 4-6 4" fill="none" stroke="#f0641e" stroke-width="2.4"/></svg>Customers with value-added service</li>
  <li><svg width="9" height="10"><path d="M1 1l6 4-6 4" fill="none" stroke="#f0641e" stroke-width="2.4"/></svg>With Kebab products,</li>
  <li><svg width="9" height="10"><path d="M1 1l6 4-6 4" fill="none" stroke="#f0641e" stroke-width="2.4"/></svg>Falafel options,</li>
  <li><svg width="9" height="10"><path d="M1 1l6 4-6 4" fill="none" stroke="#f0641e" stroke-width="2.4"/></svg>Potato variations, sweets</li>
  <li><svg width="9" height="10"><path d="M1 1l6 4-6 4" fill="none" stroke="#f0641e" stroke-width="2.4"/></svg>Beverages</li>
</ul>

<div class="abs footer">Copyright © 2011 All Rights Reserved . Privacy Statement Terms of Use,</div>
<div class="abs social" style="left:661px;background:#e8a24a"></div>
<div class="abs social" style="left:691px;background:#3a7ab0"></div>
<div class="abs social" style="left:722px;background:#6fc2e6"></div>
<div class="abs social" style="left:753px;background:#b8342a"></div>
<div class="abs social" style="left:785px;background:#d8d8e0"></div>
</body>
</html>
```